Super elegant, crisp & clean Business card design required

We recently upgraded our branding - which is on our website - tavolenstudio.com

I would like a simple, yet elegant, clean business card design please.

The font of my logo is Cinzel - and because of the natural colour - it's best to have this on a black background.

I would like to have the back of the business card - with simply my logo.

PLEASE DO NOT SUBMIT A COMPLICATED / UNCLEAN DESIGN

Industry/Entity Type

Business

Contact Information for Business Card

Danvir Okelowa Photography

Font styles to use
Other font styles liked:
• Cinzel

Requirements
Must have
• A backpage with nothing but my logo
• Simple design - stands out
Should not have
• Colour that dont align with my logo
• Over complicated '/ non symmetrical design

```html
<!DOCTYPE html>
<html lang="en">
<head>
<meta charset="utf-8">
<title>Danvir Okelowa Photography – Business Card</title>
<link rel="stylesheet" href="https://fonts.googleapis.com/css2?family=Cinzel:wght@400&family=Open+Sans:wght@400;600&display=swap">
<style>
  :root {
    --canvas: #e9e7e3;
    --ink: #000000;
    --gold: #a08d6a;
    --band: #9a8766;
    --taupe: #7f7259;
    --text-dark: #111111;
  }
  * { box-sizing: border-box; margin: 0; padding: 0; }
  html, body {
    width: 1200px; height: 900px; overflow: hidden;
    background: var(--canvas);
  }
  .canvas { position: relative; width: 1200px; height: 900px; }

  .card {
    position: absolute;
    width: 587px; height: 362px;
    overflow: hidden;
    box-shadow: 0 6px 18px rgba(0,0,0,0.18);
  }

  /* Front */
  .card-front { left: 78px; top: 35px; background: var(--taupe); }
  .front-header {
    position: absolute; left: 0; top: 0; width: 100%; height: 190px;
    background: var(--ink);
  }
  .front-accent { position: absolute; left: 0; top: 188px; width: 587px; height: 40px; }
  .brand-front {
    position: absolute; left: 0; right: 0; top: 66px; text-align: center;
    font-family: "Cinzel", serif; color: var(--gold); font-weight: 400;
  }
  .brand-front .brand-name { font-size: 36px; letter-spacing: 0.5px; line-height: 1; }
  .brand-front .brand-line { font-size: 17px; letter-spacing: 9px; margin-top: 8px; padding-left: 8px; }

  .holder {
    position: absolute; right: 315px; top: 257px; text-align: right;
    font-family: "Open Sans", sans-serif; color: var(--text-dark);
  }
  .holder .person { font-size: 18px; font-weight: 600; line-height: 1.2; }
  .holder .role { font-size: 15px; line-height: 1.4; }

  .contacts {
    position: absolute; left: 299px; top: 249px; list-style: none;
    font-family: "Open Sans", sans-serif; font-size: 15px; color: var(--text-dark);
  }
  .contacts li { display: flex; align-items: center; height: 21px; }
  .contacts svg { width: 11px; height: 11px; margin-right: 7px; fill: var(--text-dark); }
  .address {
    position: absolute; left: 104px; top: 318px;
    font-family: "Open Sans", sans-serif; font-size: 15px; color: var(--text-dark);
  }

  /* Back */
  .card-back { left: 388px; top: 500px; background: var(--taupe); }
  .back-mark {
    position: absolute; left: 50%; top: 92px; width: 70px; height: 70px;
    margin-left: -35px; border-radius: 50%; border: 2px solid var(--text-dark);
  }
  .brand-back {
    position: absolute; left: 0; right: 0; top: 236px; text-align: center;
    font-family: "Cinzel", serif; color: var(--text-dark); font-weight: 400;
  }
  .brand-back .brand-name { font-size: 27px; line-height: 1; }
  .brand-back .brand-line { font-size: 13px; letter-spacing: 7px; margin-top: 3px; padding-left: 7px; }
  .back-web {
    position: absolute; left: 0; right: 0; top: 289px; text-align: center;
    font-family: "Open Sans", sans-serif; font-size: 15px; color: var(--text-dark);
  }
</style>
</head>
<body>
<main class="canvas">

  <section class="card card-front" aria-label="Business card front">
    <div class="front-header"></div>
    <svg class="front-accent" viewBox="0 0 587 40" aria-hidden="true">
      <polygon points="0,0 412,0 382,26 0,26" fill="var(--band)"/>
      <polyline points="0,27 383,27 414,0" fill="none" stroke="#000" stroke-width="2.5"/>
    </svg>
    <div class="brand-front">
      <div class="brand-name">Danvir Okelowa</div>
      <div class="brand-line">PHOTOGRAPHY</div>
    </div>
    <div class="holder">
      <div class="person">Marcus Ellery</div>
      <div class="role">Managing Director</div>
    </div>
    <ul class="contacts">
      <li><svg viewBox="0 0 12 12" aria-hidden="true"><path d="M1 4c0-2 3-3 5-3s5 1 5 3l-2 1-1-2H4L3 5zM3 6h6l1 5H2z"/></svg>044-123 456 789</li>
      <li><svg viewBox="0 0 12 12" aria-hidden="true"><path d="M3 5V3a3 3 0 0 1 6 0v2h1v7H2V5zm2 0h2V3a1 1 0 0 0-2 0z"/></svg>info@webname.com</li>
      <li><svg viewBox="0 0 12 12" aria-hidden="true"><path d="M1 3h10v7H1zm1 1 4 3 4-3z"/></svg>www.websitename.com</li>
    </ul>
    <p class="address">12345, Address Goes Here Country Name, 123456.</p>
  </section>

  <section class="card card-back" aria-label="Business card back">
    <div class="back-mark"></div>
    <div class="brand-back">
      <div class="brand-name">Danvir Okelowa</div>
      <div class="brand-line">PHOTOGRAPHY</div>
    </div>
    <p class="back-web">www.tavolenstudio.com</p>
  </section>

</main>
</body>
</html>
```